Plakat-Design: Hausmesse Robotik und Cobots
Zielgruppe
High-Tech Engineering aus Euskirchen
Die KW Konstrukteure & Fachservice GmbH mit Sitz in Euskirchen entwickelt moderne Maschinen Robotiklösungen für Kunden in der Region, überregional und bundesweit. Mittelständische Unternehmen und Maschinenbauer, internationale Großkonzerne aus der Konsumgüterindustrie und Hersteller von Maschinen für die weiterverarbeitende Industrie vertrauen KW seit vielen Jahren.
> Maschinenbau
> Automation
> Robotik
> Certified Systemintegrator für Brennwald Mechatronik
Aufgabenstellung
Projektauftrag:
Flyer/Plakat zur Einladung Hausmesse
Format:
> Din A4 PDF zur Einladung der Kunten (digital)
> Werbebanner für E-Mail Signatur
Daten der Messe:
> 18.05.2022 10-17 Uhr
> KW Technik , Lindenhofer Weg 14, 53879 Euskirchen
> Anmeldeplattform folgt
Motto der Veranstaltung:
> 'Automation - so einfach'
> 'Einfach automatisieren mit Cobots'
> Für Vorschläge gerne offen
Was erwartet Sie:
> Roboter Demos
> Kamerageführte Robotik
> Plug & Play Lösungen
Ausstellerinformationen:
> Bitte unten Platz für Logos der Aussteller vorsehen (derzeit ca. 15)
> Logos können später übermittelt werden
Infomaterial für den Designer:
>> www.kw-technik-beispiel.de
>> www.brennwald-mechatronik-beispiel.de
>> Weitere Bilder sind vorhanden.
>> Farbeschema der PowerPoint nutzen (Vertriebspräsentation_de_KW_21-06-23.pptx)

```html
<!DOCTYPE html>
<html lang="de">
<head>
<meta charset="utf-8">
<title>Automation – so einfach · Hausmesse KW Technik</title>
<link rel="stylesheet" href="https://fonts.googleapis.com/css2?family=Raleway:wght@300;400&family=Lato:wght@700&family=Josefin+Sans:wght@400;600&display=swap">
<style>
  :root {
    --night: #070b13;
    --navy: #0f2b52;
    --blue: #13407a;
    --blue-bright: #1d5aa8;
    --sky: #4fa6dc;
    --white: #ffffff;
    --ink: #132a52;
    --panel: #c8d2dd;
    --tile: #e6ebf0;
  }
  * { margin: 0; padding: 0; box-sizing: border-box; }
  html, body { width: 848px; height: 1200px; overflow: hidden; background: var(--white); }
  .poster { position: relative; width: 848px; height: 1200px; overflow: hidden; background: var(--night); }
  .hero-art { position: absolute; left: 0; top: 0; width: 848px; height: 869px; }
  .headline { position: absolute; left: 57px; top: 78px; color: var(--white); font-family: "Raleway", sans-serif; font-weight: 300; }
  .headline-main { font-size: 80px; line-height: 1; letter-spacing: 1px; }
  .headline-sub { font-size: 46px; line-height: 1; letter-spacing: 17px; margin-top: 22px; }
  .divider { position: absolute; left: 584px; top: 86px; width: 2px; height: 130px; background: var(--sky); opacity: .8; }
  .event-date { position: absolute; right: 53px; top: 90px; text-align: right; color: var(--sky); font-family: "Josefin Sans", sans-serif; font-weight: 400; font-size: 42px; line-height: 43px; }
  .highlights { position: absolute; left: 492px; top: 707px; list-style: none; color: var(--white); font-family: "Lato", sans-serif; font-weight: 700; font-size: 20px; line-height: 28.5px; }
  .host { position: absolute; left: 0; top: 869px; width: 349px; height: 271px; background: var(--white); text-align: center; color: var(--ink); font-family: "Josefin Sans", sans-serif; }
  .host-mark { display: flex; align-items: center; justify-content: center; gap: 12px; margin-top: 52px; }
  .host-mark-square { width: 30px; height: 30px; background: var(--blue); }
  .host-name { font-family: "Josefin Sans", sans-serif; font-weight: 600; font-size: 44px; color: var(--blue); line-height: 1; }
  .host-address { margin-top: 46px; font-size: 19px; line-height: 23px; }
  .exhibitors { position: absolute; left: 349px; top: 869px; width: 499px; height: 271px; background: var(--panel); display: grid; grid-template-columns: repeat(6, 63px); grid-template-rows: repeat(3, 60px); gap: 8px 7px; padding: 39px 0 0 39px; }
  .exhibitor-slot { background: var(--tile); }
  .footer { position: absolute; left: 0; top: 1140px; width: 848px; height: 60px; background: var(--navy); color: var(--white); font-family: "Josefin Sans", sans-serif; font-weight: 600; font-size: 18px; letter-spacing: 1px; display: flex; align-items: center; justify-content: center; padding-right: 0; }
</style>
</head>
<body>
<main class="poster">
  <svg class="hero-art" viewBox="0 0 848 869" aria-hidden="false">
    <defs>
      <radialGradient id="glow" cx="0.3" cy="0.55" r="0.55">
        <stop offset="0" stop-color="#0d3a2a"/>
        <stop offset="1" stop-color="#070b13"/>
      </radialGradient>
      <linearGradient id="robot-tone" x1="0" y1="0" x2="1" y2="1">
        <stop offset="0" stop-color="#aab4bc"/>
        <stop offset="0.5" stop-color="#5c666e"/>
        <stop offset="1" stop-color="#1b1f24"/>
      </linearGradient>
    </defs>
    <rect class="backdrop" width="848" height="869" fill="url(#glow)"/>
    <polygon class="band band-upper" points="640,0 700,0 0,560 0,500" fill="var(--blue)"/>
    <polygon class="band band-thin" points="760,0 775,0 0,640 0,625" fill="var(--blue-bright)" opacity=".7"/>
    <polygon class="band band-lower" points="848,270 848,869 255,869" fill="var(--blue)"/>
    <polygon class="band band-edge" points="848,240 848,255 230,869 215,869" fill="var(--blue-bright)" opacity=".8"/>
    <path class="product-photo" role="img" aria-label="Foto eines kollaborativen Roboterarms mit Kamera und Greifer"
      d="M0,300 L90,250 L260,300 L400,360 L520,470 L560,600 L470,700 L380,700 L300,640 L220,860 L0,860 Z"
      fill="url(#robot-tone)"/>
  </svg>

  <h1 class="headline">
    <div class="headline-main">AUTOMATION</div>
    <div class="headline-sub">- SO EINFACH</div>
  </h1>
  <div class="divider"></div>
  <p class="event-date">18.05.<br>2022<br>10-17 Uhr</p>

  <ul class="highlights">
    <li>&gt; Roboter Demos</li>
    <li>&gt; Kamerageführte Robotik</li>
    <li>&gt; Plug &amp; Play Lösungen</li>
  </ul>

  <section class="host">
    <div class="host-mark">
      <span class="host-mark-square"></span>
      <span class="host-name">KW Technik</span>
    </div>
    <p class="host-address">Hausmesse der KW Technik<br>Lindenhofer Weg 14<br>53879 Euskirchen</p>
  </section>

  <section class="exhibitors" aria-label="Platz für Aussteller">
    <div class="exhibitor-slot"></div><div class="exhibitor-slot"></div><div class="exhibitor-slot"></div>
    <div class="exhibitor-slot"></div><div class="exhibitor-slot"></div><div class="exhibitor-slot"></div>
    <div class="exhibitor-slot"></div><div class="exhibitor-slot"></div><div class="exhibitor-slot"></div>
    <div class="exhibitor-slot"></div><div class="exhibitor-slot"></div><div class="exhibitor-slot"></div>
    <div class="exhibitor-slot"></div><div class="exhibitor-slot"></div><div class="exhibitor-slot"></div>
    <div class="exhibitor-slot"></div><div class="exhibitor-slot"></div><div class="exhibitor-slot"></div>
  </section>

  <footer class="footer">www.kw-technik-beispiel.de</footer>
</main>
</body>
</html>
```